Voltarey - Flyer design

Description -
Motorhome and Caravan EWOFs
Recreational Vehicles (such as caravans, motorhomes, RVs, Boats etc) and Relocatable buildings that can be connected to an electricity supply must be regularly checked for electrical safety. An EWOF needs to be issued every 4 years.
Pre-purchase house inspections
A pre-purchase electrical inspection prior to buying a home can be used to identify any dangerous and unsafe electrical parts of the installation that may be costly to repair once the property has been purchased. Giving you peace of mind when buying your new home.
High risk Electrical inspections
All Prescribed Electrical Work that falls under the High Risk category must be inspected by a Registered Electrical Inspector and have a Record of Inspection certificate issued.
Electric Vehicle Chargers
Any electrical vehicle charger that can be accessed by the public (ie in a non-domestic situation) must be periodically inspected and certified every 12 months.
General Electrical Services
Domestic and commercial - We do new builds, Renovations, Maintenance and more!
Dean Fowler - Electrician and Electrical Inspector
Ph - 0227839152
Dean@voltarey.co.nz
Auckland
------
I also want there to be a few symbols similar to the files I have attached.
The main areas that I am hoping to find work is with caravans/motohomes and EV car chargers so these symbols are quite important.
Thanks so much

```html
<!DOCTYPE html>
<html lang="en">
<head>
<meta charset="utf-8">
<title>Voltarey – Flyer</title>
<link rel="stylesheet" href="https://fonts.googleapis.com/css2?family=Montserrat:wght@400;600;700;800&family=Open+Sans:wght@400;600&display=swap">
<style>
  :root{
    --green:#7dbb2a;
    --green-dark:#5e9a17;
    --charcoal:#4a4d52;
    --charcoal-dark:#35383c;
    --text:#3c3f44;
    --muted:#6b6f75;
    --paper:#ffffff;
    --line:#d9dcdf;
  }
  *{box-sizing:border-box;margin:0;padding:0}
  html,body{width:900px;height:1200px;overflow:hidden;background:var(--paper)}
  body{font-family:"Open Sans",Arial,sans-serif;color:var(--text);position:relative}

  .flyer{position:relative;width:900px;height:1200px;background:var(--paper)}

  .header-stripes{position:absolute;top:0;right:0;width:520px;height:130px}

  .brand{position:absolute;top:46px;left:56px;display:flex;align-items:center;gap:12px}
  .brand-mark{width:34px;height:34px;border-radius:50%;background:var(--green)}
  .brand-name{font-family:"Montserrat",Arial,sans-serif;font-weight:800;font-size:34px;color:var(--charcoal);letter-spacing:-0.5px}
  .brand-tag{position:absolute;top:92px;left:102px;font-family:"Montserrat",Arial,sans-serif;font-size:12px;font-weight:600;color:var(--muted);letter-spacing:2px;text-transform:uppercase}

  .hero-photo{position:absolute;top:140px;left:56px;width:788px;height:330px;
    background:linear-gradient(120deg,#8f9aa3 0%,#c9cfd3 35%,#e07a2e 55%,#b9c0c5 70%,#6f7a83 100%)}
  .hero-band{position:absolute;top:470px;left:56px;width:788px;height:34px}

  .services{position:absolute;top:536px;left:56px;width:788px}
  .service{display:flex;gap:22px;margin-bottom:24px;align-items:flex-start}
  .service-icon{flex:0 0 78px;height:78px}
  .service-body{flex:1;border-bottom:1px solid var(--line);padding-bottom:14px}
  .service-title{font-family:"Montserrat",Arial,sans-serif;font-weight:700;font-size:19px;color:var(--green-dark);margin-bottom:4px}
  .service-text{font-size:13px;line-height:1.5;color:var(--text)}

  .footer{position:absolute;left:0;bottom:0;width:900px;height:70px}
  .footer-phone{position:absolute;right:56px;bottom:18px;background:var(--charcoal-dark);color:#fff;
    font-family:"Montserrat",Arial,sans-serif;font-weight:700;font-size:24px;padding:10px 22px;letter-spacing:1px}
</style>
</head>
<body>
<div class="flyer">

  <svg class="header-stripes" viewBox="0 0 520 130" aria-hidden="true">
    <polygon points="150,0 520,0 520,70 210,70" fill="var(--green)"/>
    <polygon points="230,80 520,80 520,100 250,100" fill="var(--charcoal)"/>
  </svg>

  <div class="brand">
    <span class="brand-mark"></span>
    <span class="brand-name">Voltarey</span>
  </div>
  <div class="brand-tag">Electrical Inspections</div>

  <div class="hero-photo" role="img" aria-label="Electrician in orange gloves working on a switchboard"></div>
  <svg class="hero-band" viewBox="0 0 788 34" preserveAspectRatio="none" aria-hidden="true">
    <rect x="0" y="0" width="788" height="34" fill="var(--charcoal)"/>
    <polygon points="0,0 520,0 490,34 0,34" fill="var(--green)"/>
  </svg>

  <section class="services">
    <article class="service">
      <svg class="service-icon" viewBox="0 0 78 78" aria-hidden="true">
        <rect width="78" height="78" fill="var(--charcoal)"/>
        <polygon points="0,78 24,78 0,54" fill="var(--green)"/>
        <rect x="14" y="26" width="46" height="24" rx="4" fill="none" stroke="#fff" stroke-width="3"/>
        <rect x="22" y="32" width="12" height="8" fill="#fff"/>
        <line x1="60" y1="44" x2="68" y2="44" stroke="#fff" stroke-width="3"/>
        <circle cx="34" cy="54" r="5" fill="#fff"/>
      </svg>
      <div class="service-body">
        <h2 class="service-title">Motorhome and Caravan EWOFs</h2>
        <p class="service-text">Recreational Vehicles (such as caravans, motorhomes, RVs, Boats etc) and Relocatable buildings that can be connected to an electricity supply must be regularly checked for electrical safety. An EWOF needs to be issued every 4 years.</p>
      </div>
    </article>

    <article class="service">
      <svg class="service-icon" viewBox="0 0 78 78" aria-hidden="true">
        <rect width="78" height="78" fill="var(--charcoal)"/>
        <polygon points="0,78 24,78 0,54" fill="var(--green)"/>
        <polygon points="39,18 62,38 16,38" fill="none" stroke="#fff" stroke-width="3" stroke-linejoin="round"/>
        <rect x="22" y="38" width="34" height="22" fill="none" stroke="#fff" stroke-width="3"/>
        <rect x="34" y="46" width="10" height="14" fill="#fff"/>
      </svg>
      <div class="service-body">
        <h2 class="service-title">Pre-purchase house inspections</h2>
        <p class="service-text">A pre-purchase electrical inspection prior to buying a home can be used to identify any dangerous and unsafe electrical parts of the installation that may be costly to repair once the property has been purchased. Giving you peace of mind when buying your new home.</p>
      </div>
    </article>

    <article class="service">
      <svg class="service-icon" viewBox="0 0 78 78" aria-hidden="true">
        <rect width="78" height="78" fill="var(--charcoal)"/>
        <polygon points="0,78 24,78 0,54" fill="var(--green)"/>
        <polygon points="43,14 24,42 37,42 32,64 54,34 41,34" fill="#fff"/>
      </svg>
      <div class="service-body">
        <h2 class="service-title">High risk Electrical inspections</h2>
        <p class="service-text">All Prescribed Electrical Work that falls under the High Risk category must be inspected by a Registered Electrical Inspector and have a Record of Inspection certificate issued.</p>
      </div>
    </article>

    <article class="service">
      <svg class="service-icon" viewBox="0 0 78 78" aria-hidden="true">
        <rect width="78" height="78" fill="var(--charcoal)"/>
        <polygon points="0,78 24,78 0,54" fill="var(--green)"/>
        <rect x="20" y="16" width="24" height="46" rx="3" fill="none" stroke="#fff" stroke-width="3"/>
        <polygon points="34,24 26,38 32,38 29,50 38,34 32,34" fill="#fff"/>
        <path d="M44 30 h8 v22 a4 4 0 0 0 8 0 v-14" fill="none" stroke="#fff" stroke-width="3"/>
      </svg>
      <div class="service-body">
        <h2 class="service-title">Electric Vehicle Chargers</h2>
        <p class="service-text">Any electrical vehicle charger that can be accessed by the public (ie in a non-domestic situation) must be periodically inspected and certified every 12 months.</p>
      </div>
    </article>

    <article class="service">
      <svg class="service-icon" viewBox="0 0 78 78" aria-hidden="true">
        <rect width="78" height="78" fill="var(--charcoal)"/>
        <polygon points="0,78 24,78 0,54" fill="var(--green)"/>
        <line x1="24" y1="56" x2="48" y2="32" stroke="#fff" stroke-width="6" stroke-linecap="round"/>
        <circle cx="52" cy="27" r="9" fill="none" stroke="#fff" stroke-width="4"/>
      </svg>
      <div class="service-body">
        <h2 class="service-title">General Electrical Services</h2>
        <p class="service-text">Domestic and commercial - We do new builds, Renovations, Maintenance and more!</p>
      </div>
    </article>
  </section>

  <svg class="footer" viewBox="0 0 900 70" preserveAspectRatio="none" aria-hidden="true">
    <polygon points="0,20 620,20 600,70 0,70" fill="var(--green)"/>
    <polygon points="620,20 900,20 900,70 600,70" fill="var(--charcoal)"/>
  </svg>
  <div class="footer-phone">0227839152</div>

</div>
</body>
</html>
```